MR Business Card

I want to create a simple business card.
I am a consultant. I design and develop furniture, lighting and accessories for hospitality and retail brands.
I want the card to be simple and clean. Not too much of a logo - but it needs the basic information shown on the attached file.
Also - I have shown some fonts that I like on the attached file.
The card can be square or rectangle. It should be double sided.
I prefer 1-2 colors (not too colorful - but using color an an accent) Even if using color on the edges as an accent.

My snapgrove link shows some other graphics styles that I like. I like clean and simple.
http://www.snapgrove-boards.net/marenrosko/business-cards/

```html
<!DOCTYPE html>
<html lang="en">
<head>
<meta charset="utf-8">
<title>Maren Rosko — Business Card</title>
<link rel="stylesheet" href="https://fonts.googleapis.com/css2?family=Questrial&family=Arimo:wght@400&display=swap">
<style>
  :root {
    --page: #ffffff;
    --ink: #231f20;
    --frame: #231f20;
    --taupe: #9c8b8e;
    --linen: #e6ddd1;
  }
  * { box-sizing: border-box; margin: 0; padding: 0; }
  html, body {
    width: 1200px;
    height: 604px;
    overflow: hidden;
    background: var(--page);
  }
  .sheet {
    position: relative;
    width: 1200px;
    height: 604px;
  }
  .card {
    position: absolute;
    top: 0;
    width: 561px;
    height: 561px;
    border: 7px solid var(--frame);
  }
  .card--front { left: 0; background: var(--page); }
  .card--back  { left: 639px; background: var(--linen); }

  .name {
    position: absolute;
    left: 296px;
    top: 425px;
    transform: rotate(-90deg);
    transform-origin: left top;
    font-family: "Arimo", Arial, sans-serif;
    font-size: 25px;
    letter-spacing: 0.22em;
    white-space: nowrap;
    color: var(--ink);
    display: flex;
    align-items: center;
    gap: 18px;
  }
  .name__mark {
    width: 16px;
    height: 16px;
    background: var(--taupe);
  }
  .tagline {
    position: absolute;
    left: 294px;
    top: 484px;
    font-family: "Questrial", "Century Gothic", sans-serif;
    font-size: 29px;
    color: var(--ink);
    white-space: nowrap;
  }

  .contact {
    position: absolute;
    left: 30px;
    top: 50px;
    font-family: "Questrial", "Century Gothic", sans-serif;
    font-size: 32px;
    line-height: 1.08;
    color: var(--ink);
  }
  .services {
    position: absolute;
    left: 12px;
    right: 10px;
    bottom: 14px;
    font-family: "Arimo", Arial, sans-serif;
    font-size: 27px;
    color: var(--ink);
    white-space: nowrap;
  }
  .services .dot { font-size: 22px; }
</style>
</head>
<body>
  <main class="sheet">
    <section class="card card--front" aria-label="Card front">
      <div class="name">
        <span>MAREN&nbsp;&nbsp;ROSKO</span>
        <span class="name__mark" aria-hidden="true"></span>
      </div>
      <p class="tagline">hospitality &amp; home</p>
    </section>

    <section class="card card--back" aria-label="Card back">
      <p class="contact">
        maren@marenrosko.com<br>
        917.555.0148
      </p>
      <p class="services">ff&amp;e<span class="dot">•</span>furniture<span class="dot">•</span>lighting<span class="dot">•</span>textiles<span class="dot">•</span> etc</p>
    </section>
  </main>
</body>
</html>
```